Author (selfpublisher) needs a book cover for thriller/crime novel

I have published a thriller / crime novel two month ago (a book in german language). The readers feedback is very positive for the story but is very weak for the existing cover. So I want to change the cover.
The title is "WIBBELT-TANGO.DE" (the "Dollart" is a bay in the north-west of Germany / has nothing to do with the US currency).

The style of the crime story is between thriller and a cosy crime story. There is some sexuality in it, of course some violence but also an amount of humor.

Important is that the story has not an urban background. The story takes place: countryside - in and around a small town / at the sea / at a lake. The landscape must be absolutely flat (no hills). The story is a so called 'regional crime story' which takes place in the north-west region of Germany, a region called 'East Frisia' or on german 'Ostfriesland'. A region with a coast, some lakes, very wide, absolutely flat landscape. Many readers of the book live here or spent holidays here.

The main character is a young private investigator without experience who is also a professional blues guitarist. With his band he is preparing a small concert tour in Germany with a well known band from the US. At that time he gets his first serious job as a private investigator. After two years of missing the dead body of a young woman is be found in a lake called 'Großes Meer'. It seems that she has offered sex for money on a dating website 'wibbelt-tango.de'. There she has met her murder who is a successful business man but also a real psycho with a disturbing character.

I still like the existing cover (please look at brimora), but mainly all readers feedbacks were bad with that. Okay, in the meantime I see, that the existing cover deals to much about sexuality. The title of the book is very sexual but the novel is less sexual! But a peaceful landscape maybe still is a good idea. Maybe with a symbol like a boat or a guitar? I am very open ...

Update:
The direction now leads clearly to a cover style that should be a friendly contrast to the hard and agressive title. It should have a nice warm atmosphere. So, cover designs that support/confirm/underline the title (in particular with a young sexy woman) will not have a chance to win,

Target Market(s)

Target market is Germany. The readers are people between 20 and 60. More women than men. Readers who like thrillers and crime novels without too much blood or violence.

Font styles to use
Other font styles liked:
• maybe typical thriller type of font? Should be easy to read on a thumbnail picture

Requirements
Must have
• This is my debut as an author, so I think the title of the book should be bigger and the author name smaller.
• A small subtitle "Ostfrieslandkrimi" must appear.
• Bar code must appear on back side.
• ---------
• What I need is finally a PDF for the whole cover printing and a high res. JPG for the e-book-version. (I have knowledge on working with the scirbus software, so I could convert the PDF on my own.)
Nice to have
• maybe a symbol from the story:
• - rowing boat ?
• - guitar ? (could be dobro style)
• - there is also a deadly car chase through a heavy storm in the story
• - if there is a landscape in your design, it should have a look of summer
Should not have
• - too much blood
• - too much sex
• - a landscape that does not fit to the East Frisian region (no hills, no cliffs, no big waves at a beach, no buildings that do not fit, a winter landscape

```html
<!DOCTYPE html>
<html lang="de">
<head>
<meta charset="utf-8">
<title>WIBBELT-TANGO.DE – Ostfrieslandkrimi</title>
<link rel="stylesheet" href="https://fonts.googleapis.com/css2?family=Oswald:wght@500;600&display=swap">
<style>
  :root {
    --stage: #e4e5e6;
    --cover-top: #1e2630;
    --cover-mid: #22303f;
    --cover-deep: #141a22;
    --ink: #ffffff;
    --wood-light: #c98d52;
    --wood-dark: #7a4a24;
    --guitar-blue: #24407a;
  }
  html, body {
    margin: 0;
    width: 1200px;
    height: 1200px;
    overflow: hidden;
    background: var(--stage);
  }
  .stage {
    position: relative;
    width: 1200px;
    height: 1200px;
  }
  .cover {
    position: absolute;
    left: 218px;
    top: 40px;
    width: 764px;
    height: 1120px;
    overflow: hidden;
    background:
      radial-gradient(ellipse 70% 30% at 60% 32%, rgba(60,90,120,0.45), transparent 70%),
      linear-gradient(180deg, var(--cover-top) 0%, var(--cover-mid) 35%, var(--cover-deep) 100%);
  }
  .cover-photo {
    position: absolute;
    left: 0;
    top: 390px;
    width: 764px;
    height: 560px;
    background:
      radial-gradient(ellipse 28% 22% at 30% 52%, rgba(36,64,122,0.95), transparent 75%),
      radial-gradient(ellipse 62% 40% at 42% 50%, var(--wood-light) 0%, var(--wood-dark) 55%, transparent 80%),
      radial-gradient(ellipse 80% 55% at 40% 50%, rgba(50,40,30,0.6), transparent 80%);
  }
  .cover-title {
    position: absolute;
    left: 0;
    top: 40px;
    width: 764px;
    height: 480px;
  }
  .cover-title text {
    fill: var(--ink);
    font-family: "Oswald", sans-serif;
  }
  .title-line {
    font-weight: 600;
    font-size: 210px;
  }
  .subtitle {
    font-weight: 500;
    font-size: 40px;
  }
  .author {
    position: absolute;
    left: 0;
    right: 0;
    top: 1000px;
    margin: 0;
    text-align: center;
    color: var(--ink);
    font-family: "Oswald", sans-serif;
    font-weight: 500;
    font-size: 44px;
    letter-spacing: 0.5px;
  }
</style>
</head>
<body>
<main class="stage">
  <section class="cover">
    <div class="cover-photo" role="img" aria-label="Bow of a wooden rowing boat with a blue electric guitar lying inside, on calm dark water"></div>
    <svg class="cover-title" viewBox="0 0 764 480" aria-label="WIBBELT-TANGO.DE – Ostfrieslandkrimi">
      <text class="title-line" x="54" y="200" textLength="656" lengthAdjust="spacingAndGlyphs">WIBBELT-</text>
      <text class="title-line" x="54" y="395" textLength="600" lengthAdjust="spacingAndGlyphs">TANGO.DE</text>
      <text class="subtitle" x="56" y="462" textLength="608" lengthAdjust="spacing">OSTFRIESLANDKRIMI</text>
    </svg>
    <p class="author">Jannis Oltmann</p>
  </section>
</main>
</body>
</html>
```